Club sale for moms — 3 static banners

Toddla is the largest daily deal site for moms, kids and babies in Russia, which provides offers with discounts up to 70%.
We need 3 banners for our flash sale, all banners must be on a white background, all must be static and be in 2 versions, so when you hover over banner the picture changes. Banners' style should differ from other banners which refer to deals (like bimbly's banners "Invite a friend, earn $20", they are attached).
Purpose: filling the empty space on the main page in case of absence of the necessary number of deals' banners. The example of our main page is attached.
1st static banner:
474px × 308px
text: Пригласите друга — получите бонус на следующую покупку!
That text means: Invite a friend and get a bonus for shopping.
After clicking on that banner a client will go to the site section "Invites".
The text means: Invite a friend and get a bonus for shopping.
2nd static banner:
308px × 199px
Text: Доставка по всей России. Оплата при получении.
After clicking on that banner a client will go to the site section about delivery.
The text means: Delivery all over Russia, pay on getting.
3rd static banner:
308px × 199px
Text:
Гарантия лучшей цены!
The text means:
Best price guarantee
Target Market(s)
moms
Industry/Entity Type
Club
Look and feel
Each slider illustrates characteristics of the customer's brand and the style your logo design should communicate.

```html
<!DOCTYPE html>
<html lang="ru">
<head>
<meta charset="utf-8">
<title>Статичные баннеры для клуба распродаж</title>
<link href="https://fonts.googleapis.com/css2?family=PT+Sans:wght@400;700&display=swap" rel="stylesheet">
<style>
  :root {
    --stage: #5d585c;
    --paper: #ffffff;
    --magenta: #c4276f;
    --magenta-dark: #9c1a55;
    --grey-text: #6b6b6b;
    --gold: #f2c45a;
    --shield-edge: #c9c9c7;
    --icon-grey: #8a8a8a;
  }
  * { margin: 0; padding: 0; box-sizing: border-box; }
  html, body { width: 1200px; height: 900px; overflow: hidden; }
  body {
    background: var(--stage);
    font-family: "PT Sans", Arial, sans-serif;
    font-weight: 400;
    position: relative;
  }
  h2, p { font-weight: 400; }
  .banner {
    position: absolute;
    background: var(--paper);
    overflow: hidden;
  }
  .banner--invite-plain { left: 26px; top: 49px; width: 392px; height: 476px; }
  .banner--invite-bonus { left: 435px; top: 49px; width: 392px; height: 476px; }
  .banner--delivery     { left: 863px; top: 49px; width: 308px; height: 199px; }
  .banner--delivery-pay { left: 863px; top: 265px; width: 308px; height: 199px; }
  .banner--price-plain  { left: 108px; top: 566px; width: 308px; height: 199px; }
  .banner--price-ribbon { left: 430px; top: 566px; width: 308px; height: 199px; }

  .invite-title {
    position: absolute; left: 26px; top: 23px;
    font-size: 40px; color: var(--magenta); line-height: 1; white-space: nowrap;
  }
  .invite-sub {
    position: absolute; left: 26px; top: 74px;
    font-size: 24px; line-height: 31px; color: var(--grey-text);
  }
  .bonus-badge { position: absolute; left: 130px; top: 140px; }
  .photo {
    position: absolute;
    background: radial-gradient(ellipse at 50% 45%, #9aa3ad 0%, #6c7c95 40%, #c9cbd0 75%, rgba(255,255,255,0) 100%);
  }
  .photo--hug { left: 144px; top: 139px; width: 248px; height: 337px; border-radius: 40% 40% 0 0; }
  .photo--stand {
    left: 155px; top: 100px; width: 210px; height: 360px; border-radius: 45% 45% 20% 20%;
    background: radial-gradient(ellipse at 60% 40%, #c9473f 0%, #4f6d94 45%, #d8d3cc 78%, rgba(255,255,255,0) 100%);
  }

  .map {
    position: absolute; left: 12px; top: 8px; width: 290px; height: 190px;
    border-radius: 30% 40% 35% 30%;
    background: linear-gradient(100deg, #d9d2f2 0%, #f6e6c6 30%, #e3f5d2 55%, #f6dbe4 75%, #d6e8f6 100%);
    opacity: .75;
  }
  .delivery-title {
    position: absolute; left: 17px; top: 59px;
    font-size: 41px; line-height: 40px; color: var(--magenta); white-space: nowrap;
  }
  .bus-icon { position: absolute; left: 238px; top: 48px; }
  .pay-note {
    position: absolute; left: 18px; top: 141px;
    display: flex; align-items: center; gap: 6px;
    font-size: 21px; color: var(--grey-text); white-space: nowrap;
  }
  .rub-dot {
    width: 19px; height: 19px; border-radius: 50%;
    background: var(--magenta); color: var(--paper);
    font-size: 13px; font-weight: 700; line-height: 19px; text-align: center;
  }

  .shield { position: absolute; left: 55px; top: 12px; }
  .price-text {
    position: absolute; left: 0; width: 100%; top: 84px;
    text-align: center; font-size: 41px; line-height: 40px;
  }
  .price-text--magenta { color: var(--magenta); }
  .price-text--grey { color: var(--grey-text); }
  .ribbon { position: absolute; left: 5px; top: 30px; }
  .ribbon-label {
    position: absolute; left: 0; width: 100%; top: 32px;
    text-align: center; font-size: 38px; color: var(--paper); line-height: 1;
  }
</style>
</head>
<body>

<section class="banner banner--invite-plain">
  <h2 class="invite-title">Пригласите друга</h2>
  <div class="photo photo--hug" role="img" aria-label="Фотография: два мальчика обнимаются, сидя на скамейке"></div>
</section>

<section class="banner banner--invite-bonus">
  <h2 class="invite-title">Пригласите друга</h2>
  <p class="invite-sub">получите бонус<br>на следующую<br>покупку!</p>
  <svg class="bonus-badge" width="40" height="44" viewBox="0 0 40 44" aria-hidden="true">
    <path d="M10 28 L4 42 L12 38 L16 44 L20 30 Z M30 28 L36 42 L28 38 L24 44 L20 30 Z" fill="#e86aa6"/>
    <circle cx="20" cy="18" r="16" fill="#d83d88"/>
    <path d="M10 12 h3 l3 10 h9 l3 -7 h-14" fill="none" stroke="#fff" stroke-width="2"/>
    <circle cx="17" cy="26" r="1.8" fill="#fff"/><circle cx="24" cy="26" r="1.8" fill="#fff"/>
  </svg>
  <div class="photo photo--stand" role="img" aria-label="Фотография: два улыбающихся мальчика стоят в обнимку"></div>
</section>

<section class="banner banner--delivery">
  <div class="map" role="img" aria-label="Разноцветная карта регионов"></div>
  <svg class="bus-icon" width="32" height="34" viewBox="0 0 32 34" aria-hidden="true">
    <rect x="3" y="2" width="26" height="26" rx="7" fill="#fff" stroke="var(--icon-grey)" stroke-width="3"/>
    <line x1="16" y1="3" x2="16" y2="16" stroke="var(--icon-grey)" stroke-width="3"/>
    <line x1="4" y1="16" x2="28" y2="16" stroke="var(--icon-grey)" stroke-width="3"/>
    <circle cx="9" cy="22" r="2" fill="var(--icon-grey)"/><circle cx="23" cy="22" r="2" fill="var(--icon-grey)"/>
    <rect x="6" y="28" width="5" height="5" fill="var(--icon-grey)"/><rect x="21" y="28" width="5" height="5" fill="var(--icon-grey)"/>
  </svg>
  <h2 class="delivery-title">Доставка по<br>всей России</h2>
</section>

<section class="banner banner--delivery-pay">
  <div class="map" role="img" aria-label="Разноцветная карта регионов"></div>
  <svg class="bus-icon" width="32" height="34" viewBox="0 0 32 34" aria-hidden="true">
    <rect x="3" y="2" width="26" height="26" rx="7" fill="#fff" stroke="var(--icon-grey)" stroke-width="3"/>
    <line x1="16" y1="3" x2="16" y2="16" stroke="var(--icon-grey)" stroke-width="3"/>
    <line x1="4" y1="16" x2="28" y2="16" stroke="var(--icon-grey)" stroke-width="3"/>
    <circle cx="9" cy="22" r="2" fill="var(--icon-grey)"/><circle cx="23" cy="22" r="2" fill="var(--icon-grey)"/>
    <rect x="6" y="28" width="5" height="5" fill="var(--icon-grey)"/><rect x="21" y="28" width="5" height="5" fill="var(--icon-grey)"/>
  </svg>
  <h2 class="delivery-title">Доставка по<br>всей России</h2>
  <p class="pay-note"><span class="rub-dot">₽</span>Оплата при получении</p>
</section>

<section class="banner banner--price-plain">
  <svg class="shield" width="198" height="182" viewBox="0 0 198 182" aria-hidden="true">
    <defs>
      <linearGradient id="shieldFillA" x1="0" y1="0" x2="0" y2="1">
        <stop offset="0" stop-color="#dcdcda"/><stop offset=".35" stop-color="#f4f4f3"/><stop offset="1" stop-color="#ffffff"/>
      </linearGradient>
    </defs>
    <path d="M1 1 H197 V140 L99 181 L1 140 Z" fill="url(#shieldFillA)" stroke="var(--shield-edge)" stroke-width="1.5"/>
  </svg>
  <p class="price-text price-text--magenta">лучшей<br>цены!</p>
</section>

<section class="banner banner--price-ribbon">
  <svg class="shield" width="198" height="182" viewBox="0 0 198 182" aria-hidden="true">
    <defs>
      <linearGradient id="shieldFillB" x1="0" y1="0" x2="0" y2="1">
        <stop offset="0" stop-color="#dcdcda"/><stop offset=".35" stop-color="#f4f4f3"/><stop offset="1" stop-color="#ffffff"/>
      </linearGradient>
    </defs>
    <path d="M1 1 H197 V140 L99 181 L1 140 Z" fill="url(#shieldFillB)" stroke="var(--shield-edge)" stroke-width="1.5"/>
  </svg>
  <svg class="ribbon" width="298" height="70" viewBox="0 0 298 70" aria-hidden="true">
    <path d="M2 16 H30 V66 H2 L12 41 Z" fill="var(--magenta-dark)"/>
    <path d="M296 16 H268 V66 H296 L286 41 Z" fill="var(--magenta-dark)"/>
    <rect x="20" y="1" width="258" height="52" fill="var(--magenta)"/>
    <rect x="20" y="49" width="258" height="5" fill="var(--gold)"/>
    <rect x="2" y="62" width="28" height="4" fill="var(--gold)"/>
    <rect x="268" y="62" width="28" height="4" fill="var(--gold)"/>
  </svg>
  <p class="ribbon-label">Гарантия</p>
  <p class="price-text price-text--grey">лучшей<br>цены!</p>
</section>

</body>
</html>
```